Box Truck Wrap

We need to create a design for our 26' box trucks. We want it to be very attention grabbing yet simple and we would like it to be modeled after our existing branding. The final deliverable needs to be 75DPI (Or more) at scale. The size of the wrap will be approximately 26' long and 8' tall. Colors are red white and blue. Please no stock images and we dpnt want any photos of people. Examples of other company trucks are included. We need one design for the side and also one for the back. Approx 7' x 8'

```html
<!DOCTYPE html>
<html lang="en">
<head>
<meta charset="utf-8">
<title>Ridgeline Movers – Truck Wrap</title>
<link rel="stylesheet" href="https://fonts.googleapis.com/css2?family=Josefin+Sans:wght@700&family=Archivo+Narrow:wght@600;700&display=swap">
<style>
  :root {
    --red: #f50a0a;
    --crimson: #a30b2c;
    --plum: #5a1352;
    --navy: #21155e;
    --white: #ffffff;
  }
  html, body {
    margin: 0;
    width: 1200px;
    height: 822px;
    overflow: hidden;
    background: var(--white);
  }
  .canvas { position: relative; width: 1200px; height: 822px; }
  .side-panel { position: absolute; left: 37px; top: 37px; width: 1126px; height: 346px; }
  .back-panel { position: absolute; left: 448px; top: 438px; width: 303px; height: 347px; }
  .brand-word { font-family: "Josefin Sans", sans-serif; font-weight: 700; }
  .headline-text { font-family: "Archivo Narrow", sans-serif; font-weight: 600; }
  .slogan-text { font-family: "Archivo Narrow", sans-serif; font-weight: 700; }
</style>
</head>
<body>
<div class="canvas">

  <!-- Side of truck -->
  <svg class="side-panel" viewBox="0 0 1126 346" aria-label="Truck side wrap">
    <defs>
      <linearGradient id="sideGradient" x1="0" y1="0" x2="1" y2="0">
        <stop offset="0.25" stop-color="var(--red)"/>
        <stop offset="0.48" stop-color="var(--crimson)"/>
        <stop offset="0.66" stop-color="var(--plum)"/>
        <stop offset="0.8" stop-color="var(--navy)"/>
      </linearGradient>
      <clipPath id="sideClip"><rect width="1126" height="346"/></clipPath>
    </defs>
    <g clip-path="url(#sideClip)">
      <rect class="side-background" width="1126" height="346" fill="url(#sideGradient)"/>

      <rect class="slogan-stripe" x="0" y="219" width="1126" height="33" fill="var(--white)"/>

      <rect class="mountain-range" x="0" y="290" width="760" height="56" fill="var(--navy)"
            role="img" aria-label="Navy mountain range silhouette along the lower edge"/>

      <circle class="feature-disc" cx="905" cy="237" r="191" fill="var(--white)"/>
      <path class="ground-curve" d="M676 346 Q 760 300 900 283 Q 1030 276 1126 322 V346 Z" fill="var(--navy)"/>

      <g class="feature-name">
        <text class="brand-word" x="905" y="165" font-size="54" text-anchor="middle" textLength="320" fill="var(--navy)">RIDGELINE</text>
        <text class="brand-word" x="905" y="212" font-size="34" text-anchor="middle" textLength="220" fill="var(--navy)">MOVERS</text>
      </g>

      <g class="brand-badge">
        <path class="badge-ring" d="M168 0 A150 150 0 0 1 184 92" fill="none" stroke="var(--white)" stroke-width="3"/>
        <circle cx="87" cy="79" r="90" fill="var(--navy)"/>
        <circle cx="80" cy="66" r="86" fill="var(--white)"/>
        <circle class="badge-dot" cx="93" cy="46" r="39" fill="var(--navy)"/>
        <text class="brand-word" x="9" y="103" font-size="25" textLength="164" fill="var(--red)">RIDGELINE</text>
        <text class="brand-word" x="39" y="119" font-size="14" textLength="103" fill="var(--red)">MOVERS</text>
      </g>

      <text class="brand-word" x="214" y="90" font-size="80" textLength="535" fill="var(--white)">RIDGELINE</text>
      <text class="brand-word" x="312" y="144" font-size="50" textLength="332" fill="var(--white)">MOVERS</text>

      <text class="headline-text" x="158" y="206" font-size="32" textLength="405" fill="var(--white)">LET OUR FAMILY MOVE YOURS!</text>
      <text class="slogan-text" x="69" y="246" font-size="29" textLength="583" fill="var(--navy)">LOCAL &amp; LONG DISTANCE MOVING MASTERS</text>
    </g>
  </svg>

  <!-- Back of truck -->
  <svg class="back-panel" viewBox="0 0 303 347" aria-label="Truck back wrap">
    <defs>
      <linearGradient id="backGradient" x1="0" y1="0" x2="0" y2="1">
        <stop offset="0.1" stop-color="var(--red)"/>
        <stop offset="0.4" stop-color="var(--crimson)"/>
        <stop offset="0.7" stop-color="var(--plum)"/>
        <stop offset="0.9" stop-color="var(--navy)"/>
      </linearGradient>
      <clipPath id="backClip"><rect width="303" height="347"/></clipPath>
    </defs>
    <g clip-path="url(#backClip)">
      <rect class="back-background" width="303" height="347" fill="url(#backGradient)"/>
      <circle class="outer-ring" cx="151" cy="174" r="168" fill="none" stroke="var(--white)" stroke-width="3"/>
      <circle cx="151" cy="174" r="158" fill="var(--white)"/>
      <circle cx="151" cy="178" r="150" fill="var(--navy)"/>
      <circle cx="164" cy="170" r="142" fill="var(--white)"/>
      <circle class="badge-dot" cx="154" cy="124" r="50" fill="var(--navy)"/>
      <text class="brand-word" x="151" y="206" font-size="36" text-anchor="middle" textLength="237" fill="var(--red)">RIDGELINE</text>
      <text class="brand-word" x="151" y="230" font-size="21" text-anchor="middle" textLength="147" fill="var(--red)">MOVERS</text>
    </g>
  </svg>

</div>
</body>
</html>
```